Manufacturer Needs Custom Decorative Basket Ecommerce Site

We work with local artisans in remote villages around the world to create unique and culturally authentic weaved baskets - decorative, storage, laundry, and handbags.

```html
<!DOCTYPE html>
<html lang="en">
<head>
<meta charset="utf-8">
<title>Weave Hollow — Handwoven Baskets</title>
<link rel="stylesheet" href="https://fonts.googleapis.com/css2?family=Playfair+Display:wght@700;900&family=Roboto:wght@400;500;700&display=swap">
<style>
:root{
  --orange:#f4a020;
  --orange-dark:#e08a10;
  --ink:#1d1d1d;
  --ink-soft:#2a2a2a;
  --text:#333;
  --muted:#777;
  --line:#e3e3e3;
  --white:#fff;
}
*{box-sizing:border-box;margin:0;padding:0}
html,body{width:1200px;height:3580px;overflow:hidden}
body{font-family:"Roboto",Arial,sans-serif;color:var(--text);background:var(--white);font-size:14px}
.serif{font-family:"Playfair Display",Georgia,serif}
.btn{display:inline-block;background:var(--orange);color:var(--white);font-weight:700;font-size:13px;letter-spacing:.5px;padding:12px 22px;text-transform:uppercase}
.accent{color:var(--orange)}

/* top bar */
.topbar{height:36px;background:var(--ink);display:flex;align-items:center;justify-content:space-between;padding:0 120px}
.topbar .dots{display:flex;gap:8px}
.topbar .dots span{width:20px;height:20px;border-radius:50%;background:var(--orange)}
.topbar .greet{color:var(--white);font-size:13px;display:flex;align-items:center;gap:8px}
.topbar .greet i{width:20px;height:20px;border-radius:50%;background:#888;display:inline-block}

/* header */
.header{height:118px;padding:0 120px;position:relative}
.brand{position:absolute;left:120px;top:16px;display:flex;align-items:center;gap:10px}
.brand .mark{width:46px;height:46px;border-radius:50%;background:var(--orange)}
.brand .name{font-family:"Playfair Display",Georgia,serif;font-weight:700;font-size:22px;color:var(--ink);line-height:1.05;text-transform:uppercase}
.header .info{position:absolute;left:310px;top:14px;display:flex;gap:28px;font-size:12px;color:var(--text)}
.header .info b{color:var(--ink)}
.header .account{position:absolute;right:120px;top:14px;display:flex;gap:30px;font-size:12px;color:var(--ink)}
.search{position:absolute;left:400px;top:56px;width:480px;height:40px;border:1px solid var(--line);display:flex}
.search .field{flex:1;padding:12px;color:#999;font-size:12px}
.search .cat{background:var(--orange);color:var(--white);font-size:12px;font-weight:700;padding:12px 18px}
.tools{position:absolute;right:120px;top:62px;display:flex;gap:18px;align-items:center}

/* nav */
.nav{height:26px;background:var(--orange);padding:0 320px;display:flex}
.nav a{display:block;background:var(--ink);color:var(--white);font-size:12px;font-weight:700;padding:6px 18px;text-decoration:none}
.nav a.active{background:#000}

/* hero */
.hero{height:510px;position:relative;background:linear-gradient(100deg,#6b5a45 0%,#9a7f5d 30%,#c84a6a 55%,#3fa3a8 75%,#e0b33f 100%)}
.hero .copy{position:absolute;left:120px;top:150px;color:var(--white)}
.hero h1{font-family:"Playfair Display",Georgia,serif;font-size:56px;line-height:1.1;font-weight:700}
.hero .btn{margin-top:30px}
.hero .pager{position:absolute;left:120px;bottom:26px;display:flex;gap:6px}
.hero .pager span{width:8px;height:8px;border-radius:50%;background:rgba(255,255,255,.6)}
.hero .pager span:first-child{background:var(--white)}

/* about */
.about{height:500px;position:relative}
.about .photo{position:absolute;left:145px;top:80px;width:410px;height:320px;background:linear-gradient(135deg,#e04f6a,#f0b23a 45%,#2f9fb0 80%,#7a4fa0)}
.about .bar{position:absolute;left:145px;top:400px;width:410px;height:10px;background:var(--orange)}
.about .copy{position:absolute;left:620px;top:80px;width:440px}
.about h2{font-size:44px;color:var(--ink);font-weight:700}
.about p{font-size:14px;line-height:1.6;margin:18px 0 26px;color:var(--text)}

/* featured */
.featured{height:660px;background:var(--ink);text-align:center;padding-top:70px}
.featured h2{font-size:44px;color:var(--white);font-weight:900}
.products{display:flex;justify-content:center;gap:36px;margin-top:40px}
.card{width:220px;color:var(--white);font-size:14px}
.card .img{height:250px;background:var(--white);position:relative;display:flex;align-items:center;justify-content:center}
.card .img div{width:150px;height:170px;border-radius:40% 40% 30% 30%}
.card .tag{position:absolute;left:8px;top:8px;background:var(--orange);color:var(--white);font-size:11px;padding:3px 8px}
.card .add{position:absolute;left:0;right:0;bottom:0;background:var(--orange);font-size:11px;padding:6px;color:var(--white)}
.card h3{font-weight:500;font-size:15px;margin-top:16px}
.card .price{color:#ccc;margin-top:6px}
.card .stars{color:var(--orange);letter-spacing:2px;margin-top:8px;font-size:16px}
.featured .btn{margin-top:40px}

/* categories */
.cats{height:780px;position:relative}
.tile{position:absolute;color:var(--white)}
.tile .lbl{position:absolute;left:18px;top:40px}
.tile h4{font-family:"Playfair Display",Georgia,serif;font-size:22px;line-height:1.1}
.tile small{display:block;font-size:11px;font-weight:700;margin-top:14px}
.tile.big h4{font-size:38px}
.tile .kick{font-size:13px;font-weight:700;display:block;margin-bottom:8px}

/* summer */
.summer{height:310px;position:relative;background:linear-gradient(90deg,var(--orange) 0%,var(--orange) 40%,#c77b3a 60%,#3f8fa0 80%,#d9572f 100%)}
.summer .copy{position:absolute;left:120px;top:70px;color:var(--white)}
.summer .kick{font-size:13px;font-weight:700}
.summer h2{font-family:"Playfair Display",Georgia,serif;font-size:40px;line-height:1.15;margin:10px 0 24px}
.summer .btn{background:var(--white);color:var(--orange)}

/* newsletter */
.news{height:250px;position:relative}
.news .copy{position:absolute;left:120px;top:85px;width:540px}
.news h2{font-size:28px;color:var(--ink);font-weight:900;white-space:nowrap;line-height:1.2}
.news p{margin-top:10px;font-size:14px;line-height:1.5;width:420px}
.news .form{position:absolute;left:685px;top:85px}
.news .email{width:400px;height:42px;border:1px solid #ccc;padding:13px;font-size:12px;color:#999}
.news .btn{margin-top:12px}

/* footer */
.footer{height:395px;background:var(--ink);position:relative;color:#ddd}
.footer .brand{left:150px;top:70px;flex-direction:column;align-items:flex-start}
.footer .brand .name{color:var(--white)}
.social{position:absolute;left:125px;top:210px;display:flex;gap:14px}
.social span{width:40px;height:40px;border-radius:50%;border:2px solid #888}
.col{position:absolute;top:70px;font-size:12px;line-height:2}
.col h5{font-family:"Playfair Display",Georgia,serif;color:var(--white);font-size:20px;margin-bottom:12px;line-height:1.2;white-space:nowrap}
.footer .legal{position:absolute;left:120px;right:120px;bottom:0;height:50px;border-top:1px solid #333;display:flex;justify-content:space-between;align-items:center;font-size:12px}
.footer .legal div{display:flex;gap:40px}
</style>
</head>
<body>

<div class="topbar">
  <div class="dots"><span></span><span></span></div>
  <div class="greet"><i></i>Hi, Mara Ellison ▾</div>
</div>

<header class="header">
  <div class="brand"><span class="mark"></span><span class="name">Weave<br>Hollow</span></div>
  <div class="info"><span><b>Call Us:</b> 555-014-2290</span><span><b>Address:</b> 212 Reedmill Lane, Alder, USA</span><span><b>USD ▾</b></span></div>
  <div class="account"><span>Create Account</span><span>Sign In</span></div>
  <div class="search"><div class="field">Search</div><div class="cat">PRODUCT ▾</div></div>
  <div class="tools">
    <svg width="20" height="20" viewBox="0 0 20 20"><circle cx="8" cy="8" r="6" fill="none" stroke="#1d1d1d" stroke-width="2"/><line x1="12.5" y1="12.5" x2="18" y2="18" stroke="#1d1d1d" stroke-width="2"/></svg>
    <svg width="24" height="22" viewBox="0 0 24 22"><path d="M1 2h4l3 12h12l3-9H6" fill="none" stroke="#1d1d1d" stroke-width="2"/><circle cx="9" cy="19" r="2" fill="#1d1d1d"/><circle cx="19" cy="19" r="2" fill="#1d1d1d"/></svg>
    <svg width="22" height="18" viewBox="0 0 22 18"><rect y="1" width="22" height="3" fill="#1d1d1d"/><rect y="8" width="22" height="3" fill="#1d1d1d"/><rect y="15" width="22" height="3" fill="#1d1d1d"/></svg>
  </div>
</header>

<nav class="nav">
  <a class="active">HOME</a><a>ABOUT</a><a>SHOP</a><a>BLOG</a><a>WORK</a><a>CONTACT</a>
</nav>

<section class="hero" role="img" aria-label="Stacked colourful handwoven baskets">
  <div class="copy">
    <h1>SALE UP TO 50%<br>OFF EVERYTHING</h1>
    <span class="btn">Shop Now</span>
  </div>
  <div class="pager"><span></span><span></span><span></span><span></span></div>
</section>

<section class="about">
  <div class="photo" role="img" aria-label="Rows of brightly woven baskets at a market"></div>
  <div class="bar"></div>
  <div class="copy">
    <h2 class="serif">ABOUT <span class="accent">US</span></h2>
    <p>Perspiciatis unde omnis iste natus error sit voluptatem accusantium doloremque laudantium totam rem aperiam, eaque ipsa quaeab illo inventore veritatis et quasi architecto beatae vitae dicta sunt explicabo. Nemo enim ipsam voluptatem quia voluptas sit aspernatur aut odit aut fugit sed quia consequuntur magni dolores eos qui ratione voluptatem sequi nesciunt neque porro quisquam est dolorem ipsum.</p>
    <span class="btn">Learn More</span>
  </div>
</section>

<section class="featured">
  <h2 class="serif">FEATURED <span class="accent">PRODUCTS</span></h2>
  <div class="products">
    <div class="card">
      <div class="img"><span class="tag">SALE</span><div role="img" aria-label="Lidded patterned basket" style="background:linear-gradient(#2a2a2a,#b8862f)"></div></div>
      <h3>Mirim Deniquis Esstrud</h3><div class="price">$110.00 – $120.00</div><div class="stars">★★★★★</div>
    </div>
    <div class="card">
      <div class="img"><div role="img" aria-label="Woven handbag with handle" style="background:linear-gradient(#8a3a2a,#2f5fa0)"></div><span class="add">ADD TO CART</span></div>
      <h3>Mirim Deniquis Esstrud</h3><div class="price">$110.00 – $120.00</div><div class="stars">★★★★★</div>
    </div>
    <div class="card">
      <div class="img"><div role="img" aria-label="Natural storage basket" style="background:linear-gradient(#d9c3a0,#b89a6e);border-radius:10px"></div></div>
      <h3>Mirim Deniquis Esstrud</h3><div class="price">$110.00 – $120.00</div><div class="stars">★★★★★</div>
    </div>
    <div class="card">
      <div class="img"><div role="img" aria-label="Tall laundry basket" style="background:linear-gradient(#e6d2b0,#c8a878);border-radius:10px"></div></div>
      <h3>Mirim Deniquis Esstrud</h3><div class="price">$110.00 – $120.00</div><div class="stars">★★★★★</div>
    </div>
  </div>
  <span class="btn">View More</span>
</section>

<section class="cats">
  <div class="tile" role="img" aria-label="Stack of natural woven baskets" style="left:112px;top:100px;width:310px;height:210px;background:linear-gradient(135deg,#4a3020,#b07a45)">
    <div class="lbl"><h4>ARCHITECTO<br>BEATAE</h4><small>SHOP NOW →</small></div></div>
  <div class="tile" role="img" aria-label="Baskets displayed on shelves" style="left:445px;top:100px;width:310px;height:210px;background:linear-gradient(135deg,#6a4528,#d0a070)">
    <div class="lbl"><h4>ARCHITECTO<br>BEATAE</h4><small>SHOP NOW →</small></div></div>
  <div class="tile" role="img" aria-label="Colourful baskets at a stall" style="left:778px;top:100px;width:310px;height:210px;background:linear-gradient(135deg,#3a3f4a,#c85a4a 60%,#e0b04a)">
    <div class="lbl"><h4>ARCHITECTO<br>BEATAE</h4><small>SHOP NOW →</small></div></div>
  <div class="tile big" role="img" aria-label="Woven hats and baskets in a shop" style="left:112px;top:330px;width:475px;height:360px;background:linear-gradient(135deg,#5a4630,#a8916a)">
    <div class="lbl" style="left:240px;top:60px"><span class="kick">UPTO 50% OFF</span><h4>ON FIRST<br>PURCHASE</h4><small>SHOP NOW →</small></div></div>
  <div class="tile big" role="img" aria-label="Assorted baskets on display" style="left:613px;top:330px;width:475px;height:360px;background:linear-gradient(135deg,#7a6a58,#c4b095)">
    <div class="lbl" style="left:240px;top:60px"><span class="kick">UPTO 40% OFF</span><h4>ON FIRST<br>PURCHASE</h4><small>SHOP NOW →</small></div></div>
</section>

<section class="summer" role="img" aria-label="Close-up of colourful coiled basket weaves">
  <div class="copy">
    <div class="kick">SUMMER 2021 OFFERS</div>
    <h2>UPTO 50% OFF ON ALL<br>NEW PRODUCTS</h2>
    <span class="btn">Shop Now</span>
  </div>
</section>

<section class="news">
  <div class="copy">
    <h2 class="serif">SUBSCRIBE TO <span class="accent">OUR NEWSLETTER</span></h2>
    <p>Perspiciatis unde omnis iste natus error sit voluptatem accusantium doloremque laudantium totam.</p>
  </div>
  <div class="form">
    <div class="email">YOUR EMAIL ADDRESS</div>
    <span class="btn">Submit</span>
  </div>
</section>

<footer class="footer">
  <div class="brand"><span class="mark"></span><span class="name">Weave<br>Hollow</span></div>
  <div class="social"><span></span><span></span><span></span><span></span></div>
  <div class="col" style="left:430px"><h5>QUICK LINKS</h5>Home<br>About<br>Shop<br>Blog<br>News<br>Contact</div>
  <div class="col" style="left:660px"><h5>LINKS</h5>Copyright<br>Legal<br>Privacy<br>Accessibility<br>Sitemap</div>
  <div class="col" style="left:860px"><h5>CUSTOMER SUPPORT</h5>Terms of Use<br>Track Orders<br>Shipping<br>Cancellation<br>Careers<br>Site Map</div>
  <div class="legal"><span>Copyright © 2021. All rights reserved.</span><div><span>Privacy Policy</span><span>Terms and Use</span></div></div>
</footer>

</body>
</html>
```